Ledgerwise Reach - B2B Demand Generation Website Project

We need a fully functional website for www.ledgerwisereach.example. We are a B2B Demand Generation company, based in London, working with companies such as QRT, VKD, Norvex, Brindlow, Tarvo generating them sales leads for their sales teams. We run this through digital marketing newsletter promotions and have a network of websites. Content syndication, data, demand generation, online marketing. Our logo has just been redone (attached) and we have a holding page already which i would like to use the style / colours. Our logo is bright and vibrant but i dont want the site to be a rainbow. We are expensive, classy, professorial, B2B, intelligent.

Home
About Us
Our Services
Prospora & QA Technology
Intent Data
Testimonials
Contact Us
Updates

Target Market(s)

B2B Marketers (QRT, Velquarion, Tarvo, VKD, Opal Reach, Driftmoor, Harlow Quantis, Technology Companies, Data Companies, Marketing Teams, Tumbleden.

Industry/Entity Type

Marketing

Coding

Coded - Design and coding required

Number of Pages Required

5+ page

Font styles to use
Sans Serif

Requirements
Must have
• Home
About Us
Our Services
Prospora & QA Technology
Intent Data
Testimonials
Contact Us

Simple Pages.

Look classy, intelligent, data experts. I like the video homepages were the image moves at the top. Very soft animation.
Nice to have
• Websites i like:

https://www.vkd.example/
https://www.brevantor.example/
https://www.plumfieldsites.example.co.uk/

Ledgerwise Reach - The Demand Generation Company
Should not have
• Glimpsevault crap images

```html
<!DOCTYPE html>
<html lang="en">
<head>
<meta charset="utf-8">
<title>Ledgerwise Reach – The Demand Generation Company</title>
<link rel="stylesheet" href="https://fonts.googleapis.com/css2?family=Poppins:ital,wght@0,300;0,400;0,500;0,600;0,700;0,800;0,900;1,400&display=swap">
<style>
:root{
  --red:#c0282d;
  --blue:#1f74d0;
  --navy:#0b2540;
  --ink:#141414;
  --grey:#6c6c6c;
  --soft:#f6f8fc;
  --contact:#2c5ea5;
  --star:#e9c21b;
  --white:#ffffff;
}
*{box-sizing:border-box;margin:0;padding:0}
html,body{width:1200px;height:3870px;overflow:hidden}
body{position:relative;font-family:'Poppins',sans-serif;color:var(--ink);background:var(--white)}
.abs{position:absolute}

/* hero */
.hero{position:absolute;left:0;top:0;width:1200px;height:738px;
  background:radial-gradient(ellipse at 62% 45%,#2f7dbb 0%,#154a7d 35%,#0a2946 70%,#061a2e 100%)}
.brand{position:absolute;left:144px;top:68px;width:180px;text-align:center;color:var(--white);font-weight:300;font-size:25px;letter-spacing:-.3px}
.nav{position:absolute;left:377px;top:54px;width:677px;display:flex;justify-content:space-between;list-style:none}
.nav li{color:var(--white);font-size:11.5px;font-weight:500;letter-spacing:.1px;position:relative}
.nav li.active::after{content:"";position:absolute;left:0;right:0;top:21px;height:3px;background:var(--red)}
.hero-art{position:absolute;left:210px;top:265px;width:220px;height:220px;border-radius:50%;
  background:radial-gradient(circle,rgba(192,40,45,.55) 0%,rgba(192,40,45,.25) 55%,rgba(192,40,45,0) 72%)}
.hero-title{position:absolute;left:560px;top:280px;width:520px;text-align:center;font-weight:900;font-size:76px;line-height:106px;letter-spacing:-1px}
.hero-title .a{color:var(--red)}
.hero-title .b{color:var(--blue)}
.btn-ghost{position:absolute;left:722px;top:545px;width:196px;height:57px;border:2px solid var(--white);background:rgba(0,0,0,.6);
  color:var(--white);font-weight:800;font-size:17px;display:flex;align-items:center;justify-content:center;gap:7px}
.dots{position:absolute;left:1126px;top:410px;display:flex;flex-direction:column;gap:10px}
.dots span{width:10px;height:10px;border-radius:50%;background:var(--white)}
.dots span.on{background:var(--red)}

/* about */
.about-h{position:absolute;left:144px;top:790px;font-size:47px;font-weight:800;line-height:1}
.about-sub{position:absolute;left:144px;top:852px;font-size:39px;font-weight:400;line-height:1}
.about-sub .a{color:var(--red)}
.about-sub .b{color:var(--blue)}
.about-p{position:absolute;left:144px;top:930px;width:440px;font-size:14.5px;line-height:33px;color:var(--grey)}
.about-art{position:absolute;left:656px;top:807px;width:398px;height:398px;border-radius:50%;
  background:radial-gradient(circle,#ffffff 34%,#e7eef8 45%,#f3c9cb 62%,#ffffff 72%)}

/* services */
.services{position:absolute;left:0;top:1281px;width:1200px;height:646px;background:var(--soft)}
.section-title{position:absolute;left:0;width:1200px;text-align:center;font-size:48px;font-weight:800;line-height:1;letter-spacing:-.5px}
.card{position:absolute;top:1468px;height:369px}
.card .label{position:absolute;left:0;right:0;bottom:33px;text-align:center;color:var(--white);font-weight:700;font-size:17px;line-height:24px;text-transform:uppercase}
.c1{left:144px;width:301px;background:linear-gradient(180deg,#7d8b92 0%,#3a474f 55%,#151b20 100%)}
.c2{left:451px;width:299px;background:linear-gradient(180deg,#a9b1aa 0%,#666c68 55%,#1d2120 100%)}
.c3{left:756px;width:298px;background:linear-gradient(180deg,#8f9aa6 0%,#4c5560 55%,#1a1f25 100%)}

/* qa */
.qa{position:absolute;left:0;top:1927px;width:1200px;height:780px;
  background:linear-gradient(120deg,#c3d5e6 0%,#e9f0f6 40%,#9fbcd6 75%,#5d85ab 100%)}
.qa-card{position:absolute;left:144px;top:2119px;width:565px;height:394px;background:var(--white);box-shadow:0 4px 18px rgba(0,0,0,.12);text-align:center}
.qa-card h2{margin-top:34px;font-size:48px;font-weight:800;line-height:1;letter-spacing:-.5px}
.qa-card p{margin:30px auto 0;width:490px;font-size:14.5px;line-height:29px;color:var(--grey)}
.btn-red{position:absolute;left:186px;top:299px;width:194px;height:54px;background:var(--red);color:var(--white);font-weight:700;font-size:17px;display:flex;align-items:center;justify-content:center;gap:7px}

/* testimonials */
.tcol{position:absolute;top:2914px;width:310px}
.avatar{position:absolute;left:0;top:0;width:66px;height:66px;border-radius:50%;border:2px solid #e2e2e2;background:radial-gradient(circle at 50% 40%,#e9dbd2 0%,#b9a79b 70%)}
.tbody{position:absolute;left:86px;top:10px;width:222px}
.quote{font-size:11.5px;line-height:22.5px;font-style:italic;color:#9a9a9a}
.quote b{color:var(--red);font-weight:800;margin-right:8px}
.tname{margin-top:13px;font-size:9.5px;color:#444;text-transform:uppercase}
.trole{font-size:9.5px;font-style:italic;color:#555;margin-top:2px}
.stars{margin-top:17px;color:var(--star);font-size:16px;letter-spacing:4px}
.arrow{position:absolute;top:2966px;width:33px;height:33px;border-radius:50%;border:1px solid #cfcfcf;display:flex;align-items:center;justify-content:center}

/* contact */
.contact{position:absolute;left:0;top:3168px;width:1200px;height:608px;background:linear-gradient(135deg,#2e64ad 0%,#2a5a9f 100%)}
.contact h2{position:absolute;left:144px;top:102px;font-size:48px;font-weight:800;color:var(--white);line-height:1;letter-spacing:-.5px}
.field{position:absolute;background:var(--white);font-size:14.5px;color:#333;padding:14px 18px}
.btn-submit{position:absolute;left:144px;top:443px;width:206px;height:57px;background:var(--red);border:2px solid var(--white);color:var(--white);font-weight:800;font-size:16.5px;display:flex;align-items:center;justify-content:center;gap:7px}
.c-brand{position:absolute;left:700px;top:140px;width:380px;text-align:center;color:var(--white);font-weight:300;font-size:46px;letter-spacing:-.5px;line-height:1}
.c-info{position:absolute;left:760px;color:var(--white);font-size:16px;line-height:26px;display:flex;gap:14px}

/* footer */
.social{position:absolute;top:3814px;width:22px;height:22px;border-radius:50%;background:#2a2a2a}
.copy{position:absolute;right:146px;top:3814px;font-size:15px;color:#333}
</style>
</head>
<body>

<header class="hero">
  <div class="brand">ledgerwisereach</div>
  <ul class="nav">
    <li class="active">HOME</li>
    <li>ABOUT US</li>
    <li>OUR SERVICES</li>
    <li>PROSPORA &amp; QA TECHNOLOGY</li>
    <li>INTENT DATA</li>
    <li>TESTIMONIALS</li>
    <li>CONTACT US</li>
  </ul>
  <div class="hero-art" role="img" aria-label="Abstract data visual in red tones"></div>
  <h1 class="hero-title"><span class="a">LEDGERWISE</span><br><span class="b">REACH</span></h1>
  <div class="btn-ghost">GET STARTED
    <svg width="15" height="15" viewBox="0 0 16 16"><circle cx="8" cy="8" r="8" fill="#fff"/><path d="M6.5 4.5 10 8l-3.5 3.5" stroke="#000" stroke-width="2.2" fill="none"/></svg>
  </div>
  <div class="dots"><span></span><span></span><span class="on"></span><span></span><span></span></div>
</header>

<section>
  <h2 class="about-h">ABOUT</h2>
  <div class="about-sub"><span class="a">LEDGERWISE</span> <span class="b">REACH</span></div>
  <p class="about-p">Ledgerwise Reach offers multi-channel demand generation services to publishers and technology vendors through our network of lead generation websites and native speaking telemarketing agents. Whether looking for MQL, ABM or BANT campaigns, Ledgerwise Reach can assist you in delivering your demand generation strategy and generate pipeline for your sales teams and/or channel partners.</p>
  <div class="about-art" role="img" aria-label="Brand illustration in red and blue"></div>
</section>

<section class="services"></section>
<h2 class="section-title" style="top:1368px">OUR SERVICES</h2>
<div class="card c1" role="img" aria-label="Photo of an analyst reviewing charts on a monitor"><div class="label">Marketing<br>Qualified Leads<br>(MQL)</div></div>
<div class="card c2" role="img" aria-label="Photo of a professional writing notes at a desk"><div class="label">Account Based<br>Marketing Leads<br>(ABM)</div></div>
<div class="card c3" role="img" aria-label="Photo of hands typing on a laptop"><div class="label">Sales Qualified<br>Lead / BANT</div></div>

<section class="qa" role="img" aria-label="Photo of a laptop with overlaid network graphics"></section>
<div class="qa-card">
  <h2>QA TECHNOLOGY</h2>
  <p>Prospora is a proprietary lead verification platform from Ledgerwise Reach that aims to sift out invalid leads with questionable or erroneous data. The platform is designed to equip sales teams with accurate, high-quality records in order to improve lead generation, accelerate pipeline and increase revenue.</p>
  <div class="btn-red">READ MORE
    <svg width="15" height="15" viewBox="0 0 16 16"><circle cx="8" cy="8" r="8" fill="#fff"/><path d="M6.5 4.5 10 8l-3.5 3.5" stroke="#c0282d" stroke-width="2.2" fill="none"/></svg>
  </div>
</div>

<h2 class="section-title" style="top:2798px">TESTIMONIALS</h2>
<div class="arrow" style="left:67px"><svg width="10" height="12" viewBox="0 0 10 12"><path d="M7 1 2 6l5 5" stroke="#aaa" fill="none" stroke-width="1.3"/></svg></div>
<div class="arrow" style="left:1098px"><svg width="10" height="12" viewBox="0 0 10 12"><path d="M3 1l5 5-5 5" stroke="#aaa" fill="none" stroke-width="1.3"/></svg></div>

<div class="tcol" style="left:132px">
  <div class="avatar" role="img" aria-label="Client portrait"></div>
  <div class="tbody">
    <p class="quote"><b>//</b>At vero eos et accusam iustodio dignissimos ducimus qui blatiipraesnt ium voluptatum deleniti atq.</p>
    <p class="tname">Maren Holt</p>
    <p class="trole">Financial Services Professional</p>
    <p class="stars">★★★★☆</p>
  </div>
</div>
<div class="tcol" style="left:455px">
  <div class="avatar" role="img" aria-label="Client portrait"></div>
  <div class="tbody">
    <p class="quote"><b>//</b>At vero eos et accusam iustodio dignissimos ducimus qui blatiipraesnt ium voluptatum deleniti atq.</p>
    <p class="tname">Tobias R. Ellery</p>
    <p class="trole">National Urban Fellow at the Institute</p>
    <p class="stars">★★★★☆</p>
  </div>
</div>
<div class="tcol" style="left:780px">
  <div class="avatar" role="img" aria-label="Client portrait"></div>
  <div class="tbody">
    <p class="quote"><b>//</b>At vero eos et accusam iustodio dignissimos ducimus qui blatiipraesnt ium voluptatum deleniti atq.</p>
    <p class="tname">Judith Carrow</p>
    <p class="trole">Creative Strategist | Entrepreneur &amp; Upcoming</p>
    <p class="stars">★★★★☆</p>
  </div>
</div>

<section class="contact">
  <h2>HOW CAN WE HELP?</h2>
  <div class="field" style="left:144px;top:198px;width:241px;height:52px">Enter Name</div>
  <div class="field" style="left:398px;top:198px;width:239px;height:52px">Enter Email</div>
  <div class="field" style="left:144px;top:261px;width:241px;height:53px">Phone</div>
  <div class="field" style="left:398px;top:261px;width:239px;height:53px">Address</div>
  <div class="field" style="left:144px;top:324px;width:493px;height:87px">Message</div>
  <div class="btn-submit">SUBMIT MESSAGE
    <svg width="15" height="15" viewBox="0 0 16 16"><circle cx="8" cy="8" r="8" fill="#fff"/><path d="M6.5 4.5 10 8l-3.5 3.5" stroke="#c0282d" stroke-width="2.2" fill="none"/></svg>
  </div>
  <div class="c-brand">ledgerwisereach</div>
  <div class="c-info" style="top:320px">
    <svg width="12" height="17" viewBox="0 0 12 17" style="margin-top:5px"><path d="M6 0a6 6 0 0 0-6 6c0 4.5 6 11 6 11s6-6.5 6-11a6 6 0 0 0-6-6z" fill="#fff"/><circle cx="6" cy="6" r="2.3" fill="#2c5ea5"/></svg>
    <span>123,Lorem ipsum dolor sit amet<br>consectetur adipiscing</span>
  </div>
  <div class="c-info" style="top:384px">
    <svg width="14" height="14" viewBox="0 0 24 24" style="margin-top:6px"><path d="M6.6 10.8a15.1 15.1 0 0 0 6.6 6.6l2.2-2.2a1 1 0 0 1 1-.25 11.4 11.4 0 0 0 3.6.57 1 1 0 0 1 1 1V20a1 1 0 0 1-1 1A17 17 0 0 1 3 4a1 1 0 0 1 1-1h3.5a1 1 0 0 1 1 1c0 1.25.2 2.45.57 3.57a1 1 0 0 1-.25 1z" fill="#fff"/></svg>
    <span>Phone : 1 800 555 0142</span>
  </div>
</section>

<footer>
  <span class="social" style="left:162px"></span>
  <span class="social" style="left:229px"></span>
  <span class="social" style="left:297px"></span>
  <p class="copy">Copyright © 2020 Ledgerwise Reach . All Rights Reserved.</p>
</footer>

</body>
</html>
```